Web API Startup Need Wordpress site

Company Logo and color scheme are completed. Now we want to use Wordpress to publish the company overview, team members, products, press releases, a blog, contact us.

This company is a startup so we want to be smart, edgy and fun. This company's goal is to kick over some trash can's in healthcare, government, and enterprise IT web applications so we have to be professional while we challenge the status quo.

We want to use a Bootstrap theme, if possible.

Target Market(s)

Professionals and Enterprise customers looking to use the services of a web api company. This could be doctors, journalists, enterprise it departments.

Industry/Entity Type

Information Technology

Coding

Coded - Design and coding required

Font styles to use
Sans Serif

Requirements
Must have
• a portfolio view to display products, which are web applications, a page for press releases, a page for blogs, company overview and team members, places to embed videos
Nice to have
• One idea could be to have a great hero image that captures clouds, water, green grass, an individual (like the symbols in the logo);
• Great use of color is important so that the site is cool, edgy but fun tech

```html
<!DOCTYPE html>
<html lang="en">
<head>
<meta charset="utf-8">
<title>CodeHarbor — Web API Studio</title>
<link href="https://fonts.googleapis.com/css2?family=Fira+Sans:wght@300;400;500;600;700&display=swap" rel="stylesheet">
<style>
:root{
  --green:#6cc04a;
  --blue:#1fa3d8;
  --ink:#2b2b2b;
  --muted:#8a8a8a;
  --light:#f3f3f3;
  --line:#e3e3e3;
  --dark:#1c1c1c;
  --footer:#151515;
  --white:#ffffff;
}
*{box-sizing:border-box;margin:0;padding:0}
html,body{width:1200px;height:4615px;overflow:hidden}
body{font-family:"Fira Sans",Arial,sans-serif;color:var(--ink);background:var(--white);position:relative}
.container{width:966px;margin:0 auto}
/* header */
.site-header{height:70px;display:flex;align-items:center;justify-content:space-between;padding:0 80px 0 104px;background:var(--white);position:relative;z-index:2}
.brand{display:flex;align-items:center;gap:10px;font-size:22px;font-weight:700;color:var(--blue);letter-spacing:.5px;line-height:1}
.brand-mark{width:14px;height:14px;background:var(--blue)}
.main-nav{display:flex;gap:28px}
.main-nav a{font-size:12px;font-weight:600;color:var(--green);text-decoration:none;text-transform:uppercase}
.hero{height:660px;background:radial-gradient(ellipse at 22% 25%,#f5c78a 0%,#c7804a 25%,#6b4227 55%,#3a2516 100%)}
/* headings */
.section-title{text-align:center;font-size:30px;font-weight:600;color:var(--ink)}
.section-sub{text-align:center;font-size:15px;color:var(--muted);margin-top:14px;font-weight:300}
.title-rule{width:30px;height:2px;background:var(--green);margin:16px auto 0}
/* overview */
.overview{height:664px;padding-top:100px}
.overview .section-sub{width:520px;margin:14px auto 0;line-height:1.5}
.services{display:grid;grid-template-columns:repeat(3,1fr);column-gap:36px;row-gap:60px;margin-top:78px}
.service-head{display:flex;align-items:center;gap:10px;font-size:15px;font-weight:600}
.service-head svg{width:22px;height:22px;flex:none}
.service p{font-size:12.5px;line-height:1.7;color:var(--muted);margin-top:12px;padding-left:2px;font-weight:300}
/* innovation */
.innovation{height:468px;background:var(--light);padding-top:110px}
.innovation .container{display:flex}
.innov-text{width:460px}
.innov-text h2{font-size:30px;font-weight:600}
.innov-text p{font-size:12.5px;line-height:1.75;color:var(--muted);margin-top:22px;font-weight:300}
.btn-dark{display:inline-block;margin-top:34px;background:var(--ink);color:var(--white);font-size:10px;font-weight:600;text-transform:uppercase;padding:13px 40px;border-radius:20px}
.features{display:flex;margin-left:86px;margin-top:-10px}
.feature{width:250px;text-align:center;padding-top:20px}
.feature + .feature{border-left:1px solid var(--line)}
.feature-ring{width:156px;height:156px;border:2px solid var(--green);border-radius:50%;margin:0 auto;display:flex;align-items:center;justify-content:center}
.feature-ring svg{width:44px;height:44px}
.feature h3{font-size:15px;font-weight:600;margin-top:24px}
/* team */
.team{height:796px;padding-top:108px}
.team-grid{display:grid;grid-template-columns:repeat(3,302px);gap:30px;margin-top:68px}
.member-photo{height:226px}
.member h3{text-align:center;font-size:16px;font-weight:700;margin-top:36px;text-transform:uppercase}
.member .role{text-align:center;font-size:12px;color:var(--green);margin-top:10px}
.member p{text-align:center;font-size:12.5px;line-height:1.7;color:var(--muted);margin:22px 26px 0;font-weight:300}
.member-social{display:flex;justify-content:center;gap:14px;margin-top:22px}
.member-social span{width:10px;height:10px;border-radius:50%;background:#a8a8a8}
/* clients */
.clients{height:228px;background:var(--dark);display:flex;align-items:center;justify-content:center;gap:80px}
.client{font-size:30px;font-weight:500;color:#e8e8e8;display:flex;align-items:center;gap:10px}
.client i{display:block;width:14px;height:14px;border:2px solid #e8e8e8}
/* work */
.work{height:1000px;padding-top:112px}
.work-grid{display:grid;grid-template-columns:repeat(3,302px);gap:31px 30px;margin-top:78px}
.work-tile{height:302px}
/* news */
.news{height:668px;background:var(--light);padding-top:110px;position:relative}
.news-grid{display:grid;grid-template-columns:repeat(3,302px);gap:30px;margin-top:62px}
.news-card{background:var(--white);height:322px;padding:36px 36px 0}
.news-card h3{font-size:16px;font-weight:600}
.news-meta{font-size:10.5px;color:var(--muted);margin-top:14px;display:flex;gap:10px}
.news-card p{font-size:12.5px;line-height:1.7;color:var(--muted);margin-top:24px;font-weight:300}
.read-more{display:flex;align-items:center;gap:14px;margin-top:36px;font-size:12px;font-weight:600}
.carousel-dots{position:absolute;left:0;right:0;top:634px;display:flex;justify-content:center;gap:8px}
.carousel-dots span{width:22px;height:3px;background:#d7d7d7}
.carousel-dots span.active{background:var(--green)}
.carousel-arrow{position:absolute;top:404px}
/* footer */
.site-footer{height:61px;background:var(--footer);display:flex;align-items:center;justify-content:space-between;padding:0 96px 0 110px;color:#8a8a8a;font-size:11px}
.footer-social{display:flex;gap:22px}
.footer-social span{width:12px;height:12px;background:var(--green)}
</style>
</head>
<body>

<header class="site-header">
  <div class="brand"><span class="brand-mark"></span>CODEHARBOR</div>
  <nav class="main-nav">
    <a href="#">Home</a><a href="#">About Us</a><a href="#">Our Services</a><a href="#">Press Releases</a><a href="#">Blog</a><a href="#">Contact Us</a>
  </nav>
</header>

<div class="hero" role="img" aria-label="Hero photo: glowing globe with web and app icons rising above a tablet on a wooden desk"></div>

<section class="overview">
  <div class="container">
    <h2 class="section-title">Company Overview</h2>
    <p class="section-sub">We build fast, secure web APIs that help teams in health, government and enterprise move their apps forward.</p>
    <div class="services">
      <div class="service">
        <div class="service-head"><svg viewBox="0 0 24 24" fill="none" stroke="#6cc04a" stroke-width="2"><path d="M8 7l-5 5 5 5M16 7l5 5-5 5M14 5l-4 14"/></svg>Web Development</div>
        <p>Modern sites built on clean code and solid APIs, shaped around your users and ready to grow with your team.</p>
      </div>
      <div class="service">
        <div class="service-head"><svg viewBox="0 0 24 24" fill="none" stroke="#6cc04a" stroke-width="2"><circle cx="12" cy="12" r="9"/><path d="M3 12h18M12 3c3 3 3 15 0 18M12 3c-3 3-3 15 0 18"/></svg>Web Interface Design</div>
        <p>Clear, friendly interfaces that make complex data simple to read and easy to act on every single day.</p>
      </div>
      <div class="service">
        <div class="service-head"><svg viewBox="0 0 24 24" fill="none" stroke="#6cc04a" stroke-width="2"><rect x="3" y="5" width="18" height="14" rx="2"/><circle cx="12" cy="12" r="3"/></svg>Mobile Apps Development</div>
        <p>Native feeling mobile apps that connect to your services and keep working well wherever your people go.</p>
      </div>
      <div class="service">
        <div class="service-head"><svg viewBox="0 0 24 24" fill="none" stroke="#6cc04a" stroke-width="2"><rect x="3" y="4" width="18" height="13" rx="1"/><path d="M8 21h8"/></svg>Client-Side Development</div>
        <p>Responsive front ends that load quickly, stay accessible and feel smooth on every screen and browser.</p>
      </div>
      <div class="service">
        <div class="service-head"><svg viewBox="0 0 24 24" fill="none" stroke="#6cc04a" stroke-width="2"><rect x="3" y="4" width="18" height="12" rx="1"/><path d="M12 16v4M7 20h10"/></svg>Server-Side Development</div>
        <p>Reliable back ends and secure endpoints designed to scale with traffic and meet strict compliance rules.</p>
      </div>
      <div class="service">
        <div class="service-head"><svg viewBox="0 0 24 24" fill="none" stroke="#6cc04a" stroke-width="2"><rect x="3" y="6" width="18" height="14" rx="1"/><path d="M3 10h18M9 3h6v3"/></svg>Database Management</div>
        <p>Well organised data stores, backups and tuning so your records stay safe, fast and always available.</p>
      </div>
    </div>
  </div>
</section>

<section class="innovation">
  <div class="container">
    <div class="innov-text">
      <h2>Innovation Orchestration</h2>
      <p>We bring people, data and services together so new ideas ship faster. Our team blends careful engineering with a bold attitude, questioning old habits in healthcare, government and enterprise IT. We listen first, plan in short cycles and deliver tools that people actually enjoy using. Every project is open, measured and built to last well beyond launch day.</p>
      <span class="btn-dark">Read More</span>
    </div>
    <div class="features">
      <div class="feature">
        <div class="feature-ring"><svg viewBox="0 0 24 24" fill="none" stroke="#6cc04a" stroke-width="1.6"><path d="M14 4c3-1 6-1 6-1s0 3-1 6l-7 7-5-5z"/><path d="M7 11l-3 1 2 2M13 17l-1 3-2-2M6 18l-2 2"/></svg></div>
        <h3>Outstanding Support</h3>
      </div>
      <div class="feature">
        <div class="feature-ring"><svg viewBox="0 0 24 24" fill="none" stroke="#6cc04a" stroke-width="1.6"><path d="M6 4h12l3 5-9 11L3 9z"/><path d="M3 9h18M9 4l3 16M15 4l-3 16"/></svg></div>
        <h3>Proven Records</h3>
      </div>
    </div>
  </div>
</section>

<section class="team">
  <div class="container">
    <h2 class="section-title">Our Team</h2>
    <p class="section-sub">Small crew, big ideas, and a lot of coffee.</p>
    <div class="title-rule"></div>
    <div class="team-grid">
      <div class="member">
        <div class="member-photo" role="img" aria-label="Portrait photo of team member Dorian Vale" style="background:linear-gradient(135deg,#b9b3aa,#4e5f78)"></div>
        <h3>Dorian Vale</h3>
        <div class="role">Developer</div>
        <p>Builds our API core and loves tidy code, quick tests and long bike rides on weekends.</p>
        <div class="member-social"><span></span><span></span><span></span><span></span></div>
      </div>
      <div class="member">
        <div class="member-photo" role="img" aria-label="Portrait photo of team member Marco Ellison" style="background:linear-gradient(135deg,#2f2f2f,#6a5a4a)"></div>
        <h3>Marco Ellison</h3>
        <div class="role">Designer</div>
        <p>Shapes every screen we ship and turns rough ideas into simple, friendly designs.</p>
        <div class="member-social"><span></span><span></span><span></span><span></span></div>
      </div>
      <div class="member">
        <div class="member-photo" role="img" aria-label="Portrait photo of team member Tessa Marlow" style="background:linear-gradient(135deg,#d8d8d8,#3a3232)"></div>
        <h3>Tessa Marlow</h3>
        <div class="role">IT Consultant</div>
        <p>Guides clients through planning, security and rollout with calm and clear advice.</p>
        <div class="member-social"><span></span><span></span><span></span><span></span></div>
      </div>
    </div>
  </div>
</section>

<section class="clients">
  <div class="client">Ostra</div>
  <div class="client">Pixelum</div>
  <div class="client">Northwind</div>
  <div class="client"><i></i>Copperline</div>
  <div class="client">Harbor Co</div>
</section>

<section class="work">
  <div class="container">
    <h2 class="section-title">View Our Work</h2>
    <p class="section-sub">Technology with a creative touch</p>
    <div class="title-rule"></div>
    <div class="work-grid">
      <div class="work-tile" role="img" aria-label="Illustration: location-based service app" style="background:linear-gradient(180deg,#f4f1ec,#f2c86a)"></div>
      <div class="work-tile" role="img" aria-label="Illustration: mobile analytics dashboard" style="background:linear-gradient(180deg,#4a5060,#7a8a9a)"></div>
      <div class="work-tile" role="img" aria-label="Illustration: search engine marketing calculator and report" style="background:linear-gradient(180deg,#f1f3f5,#f0c85a)"></div>
      <div class="work-tile" role="img" aria-label="Photo: laptop showing business charts" style="background:linear-gradient(180deg,#5a6670,#2b3238)"></div>
      <div class="work-tile" role="img" aria-label="Photo: professional working on a laptop" style="background:linear-gradient(180deg,#c9d7b8,#d9dde2)"></div>
      <div class="work-tile" role="img" aria-label="Illustration: web technologies around a smartphone" style="background:linear-gradient(180deg,#f4f4f4,#9fce6a)"></div>
    </div>
  </div>
</section>

<section class="news">
  <div class="container">
    <h2 class="section-title">Read Our Latest News</h2>
    <p class="section-sub">Fresh notes from our team and our projects.</p>
    <div class="title-rule"></div>
    <div class="news-grid">
      <div class="news-card">
        <h3>Choosing the best</h3>
        <div class="news-meta"><span>by Ava</span><span>|</span><span>Company</span><span>|</span><span>February 24, 2016</span></div>
        <p>How we pick the right stack for each client, and why simple choices often win over shiny new tools...</p>
        <div class="read-more">Read More <svg width="26" height="10" viewBox="0 0 26 10" fill="none" stroke="#6cc04a" stroke-width="1.5"><path d="M0 5h24M20 1l4 4-4 4"/></svg></div>
      </div>
      <div class="news-card">
        <h3>Pursuing perfection</h3>
        <div class="news-meta"><span>by Ava</span><span>|</span><span>Company</span><span>|</span><span>February 24, 2016</span></div>
        <p>Small details make large differences. A look at the review habits that keep our releases steady...</p>
        <div class="read-more">Read More <svg width="26" height="10" viewBox="0 0 26 10" fill="none" stroke="#6cc04a" stroke-width="1.5"><path d="M0 5h24M20 1l4 4-4 4"/></svg></div>
      </div>
      <div class="news-card">
        <h3>Imagination at work</h3>
        <div class="news-meta"><span>by Ava</span><span>|</span><span>Company</span><span>|</span><span>February 24, 2016</span></div>
        <p>From whiteboard sketch to working product: the story behind our newest health records API...</p>
        <div class="read-more">Read More <svg width="26" height="10" viewBox="0 0 26 10" fill="none" stroke="#6cc04a" stroke-width="1.5"><path d="M0 5h24M20 1l4 4-4 4"/></svg></div>
      </div>
    </div>
  </div>
  <div class="carousel-dots"><span class="active"></span><span></span><span></span><span></span><span></span></div>
  <svg class="carousel-arrow" style="left:76px" width="12" height="20" viewBox="0 0 12 20" fill="none" stroke="#aaa" stroke-width="2"><path d="M10 2L2 10l8 8"/></svg>
  <svg class="carousel-arrow" style="left:1096px" width="12" height="20" viewBox="0 0 12 20" fill="none" stroke="#aaa" stroke-width="2"><path d="M2 2l8 8-8 8"/></svg>
</section>

<footer class="site-footer">
  <span>© 2016 CODEHARBOR. All rights reserved.</span>
  <div class="footer-social"><span></span><span></span><span></span><span></span></div>
</footer>

</body>
</html>
```